VORELT B2B portal design
Fantastic design work, top communication and fast design changes! Many thanks,Jens & Uwe from VORELT
Zielgruppe
We are a B2B Cloud Services StartUp that creates B2B logistics & supply chain processes between customer and its suppliers.
Aufgabenstellung
We need a modern responsive able design, that should consider that we are NOT presenting goods or clothes or similar on the portal pages but we show mainly data grids, kpi dashboards, forms, and setting panels to our customer and their suppliers.
The design must be clean and straight not to distract people from the important information in these data grids, kpi dashboards, forms, and settings panels.
We need our logo perfectly embedded and the pages coloured around from grey to blue.
The Designer must be able to deliver a design and transfer it to a highly responsive HTML (5) template (without technical content or further functionality). This our programmers will implement afterwards in .Net.
We need in total 3 page templates:
1. Login Page
2. Main Page with overview over the following services text (each one shown in one tile)
"ZMS (Time Frame Management)"
"DMS (Document Management)"
"REMS (Reporting Management)"
-> Note: At the end we will have up to 12 or more tiles (services) so the design should be additive
3. Data grid (e.g. list of customers)/form (e.g. customer registration form) page to show some data grid with database data
See samples for each page enclosed!!

```html
<!DOCTYPE html>
<html lang="en">
<head>
<meta charset="utf-8">
<title>VORELT – User Registration Form</title>
<link rel="stylesheet" href="https://fonts.googleapis.com/css2?family=Ubuntu:wght@400;500;700&family=Exo+2:wght@800&display=swap">
<style>
  :root {
    --navy: #0b2a45;
    --navy-text: #10304d;
    --header-bg: #e3e8ec;
    --sidebar-bg: #e3e8ec;
    --divider: #c9d0d6;
    --main-bg: #f7f8fa;
    --card-bg: #ffffff;
    --text: #333a40;
    --muted: #5c6368;
    --placeholder: #a9afb4;
    --field-border: #b9bec2;
    --field-focus: #2f6d9b;
    --success-bg: #e3f2d6;
    --success-border: #8fcf5b;
    --success-text: #3f8f1f;
    --error-bg: #f3ded6;
    --error-border: #d27a5f;
    --error-text: #b33a1d;
    --link-red: #e0261b;
    --footer-text: #444b50;
  }
  * { box-sizing: border-box; margin: 0; padding: 0; }
  html, body { width: 1200px; height: 948px; overflow: hidden; }
  body {
    position: relative;
    font-family: "Ubuntu", sans-serif;
    color: var(--text);
    background: var(--main-bg);
  }

  /* Header */
  .site-header {
    position: absolute; left: 0; top: 0; width: 1200px; height: 137px;
    background: var(--header-bg);
    border-bottom: 1px solid #b5bec6;
  }
  .brand {
    position: absolute; left: 24px; top: 46px;
    display: flex; align-items: center; gap: 12px;
    font-size: 40px; font-weight: 700; color: var(--navy-text); letter-spacing: 1px;
  }
  .brand-mark { width: 18px; height: 18px; border-radius: 50%; background: var(--navy-text); }
  .tagline {
    position: absolute; left: 306px; top: 54px;
    font-family: "Exo 2", sans-serif; font-weight: 800; font-size: 23px;
    color: var(--navy-text); letter-spacing: 3.2px; white-space: nowrap;
  }
  .user-info { position: absolute; right: 107px; top: 48px; text-align: right; }
  .user-name { font-size: 20px; font-weight: 500; color: #1d2a35; }
  .user-role { font-size: 13px; color: var(--muted); margin-top: 1px; }
  .avatar {
    position: absolute; left: 1100px; top: 35px; width: 66px; height: 66px;
    border-radius: 50%; background: radial-gradient(circle at 50% 40%, #8c8580, #3d3b3a);
    border: 2px solid #cfd5da;
  }
  .user-caret { position: absolute; left: 1172px; top: 64px; }

  /* Sidebar */
  .sidebar {
    position: absolute; left: 0; top: 137px; width: 265px; height: 708px;
    background: var(--sidebar-bg);
  }
  .nav-item {
    height: 61px; display: flex; align-items: center; padding-left: 18px; gap: 10px;
    font-size: 19px; color: #1f2a33; border-bottom: 1px solid var(--divider);
    position: relative;
  }
  .nav-item svg { width: 28px; height: 24px; flex: none; }
  .nav-item.active { background: var(--navy); color: #fff; border-bottom-color: var(--navy); }
  .nav-item .chevron { position: absolute; right: 28px; width: 12px; }
  .nav-item:last-child { border-bottom: none; }

  /* Main */
  .page-title {
    position: absolute; left: 304px; top: 186px;
    font-size: 24px; font-weight: 400; color: #4a5157;
  }
  .card {
    position: absolute; left: 305px; top: 240px; width: 870px; height: 604px;
    background: var(--card-bg); border-radius: 3px;
    box-shadow: 0 3px 0 #dde1e4;
  }
  .card-intro {
    position: absolute; left: 0; top: 45px; width: 870px; text-align: center;
    font-size: 17px; color: #2b3137;
  }
  .alert {
    position: absolute; top: 109px; width: 365px; height: 41px;
    border: 1px solid; border-radius: 2px; padding-left: 14px;
    display: flex; align-items: center; font-size: 15px;
  }
  .alert-success { left: 51px; background: var(--success-bg); border-color: var(--success-border); color: var(--success-text); }
  .alert-error { left: 447px; background: var(--error-bg); border-color: var(--error-border); color: var(--error-text); }

  .field { position: absolute; width: 260px; }
  .field label { display: block; font-size: 14px; color: var(--muted); margin-bottom: 10px; }
  .field .input {
    height: 42px; border: 1px solid var(--field-border); border-radius: 4px;
    display: flex; align-items: center; padding-left: 14px;
    font-size: 15px; color: var(--placeholder);
  }
  .field .input.filled { color: #2b3137; border-color: var(--field-focus); }
  .field .input.password { letter-spacing: 3px; font-size: 12px; }
  .field-username { left: 51px; top: 193px; }
  .field-password { left: 411px; top: 193px; width: 258px; }
  .field-mail { left: 51px; top: 306px; }
  .field-phone { left: 411px; top: 306px; width: 258px; }

  .check { position: absolute; left: 51px; display: flex; align-items: center; gap: 8px; font-size: 14px; color: #4a5157; }
  .check svg { width: 22px; height: 22px; }
  .check-terms { top: 405px; }
  .check-remember { top: 443px; }
  .check a { color: var(--link-red); text-decoration: none; }

  .btn-register {
    position: absolute; left: 57px; top: 496px; width: 119px; height: 40px;
    background: var(--navy); color: #fff; border: none; border-radius: 2px;
    font-family: "Ubuntu", sans-serif; font-size: 15px; font-weight: 500;
  }

  /* Footer */
  .site-footer {
    position: absolute; left: 0; top: 886px; width: 1200px; height: 62px;
    background: #fff; border-top: 1px solid #e1e4e7;
    font-size: 16px; color: var(--footer-text);
  }
  .copyright { position: absolute; left: 14px; top: 21px; }
  .footer-links { position: absolute; right: 24px; top: 21px; }
</style>
</head>
<body>
  <header class="site-header">
    <div class="brand"><span class="brand-mark"></span>VORELT</div>
    <div class="tagline">RELIABLE &amp; SCALABLE CLOUD SOLUTIONS</div>
    <div class="user-info">
      <div class="user-name">Lars Brenner</div>
      <div class="user-role">Gest User</div>
    </div>
    <div class="avatar" role="img" aria-label="User profile photo"></div>
    <svg class="user-caret" width="10" height="8" viewBox="0 0 10 8"><path d="M0 0h10L5 7z" fill="#6a7278"/></svg>
  </header>

  <nav class="sidebar">
    <div class="nav-item">
      <svg viewBox="0 0 28 24"><circle cx="14" cy="12" r="8" fill="none" stroke="#1f2a33" stroke-width="1.6"/><path d="M6 12h16M14 4c-4 4-4 12 0 16M14 4c4 4 4 12 0 16" fill="none" stroke="#1f2a33" stroke-width="1.2"/></svg>
      My News
    </div>
    <div class="nav-item">
      <svg viewBox="0 0 28 24"><circle cx="11" cy="7" r="5" fill="#1f2a33"/><path d="M2 22c0-6 4-9 9-9s8 2 9 5v4z" fill="#1f2a33"/><circle cx="21" cy="18" r="3.5" fill="none" stroke="#1f2a33" stroke-width="2"/></svg>
      My User Settings
    </div>
    <div class="nav-item active">
      <svg viewBox="0 0 28 24">
        <circle cx="10" cy="9" r="6" fill="none" stroke="#fff" stroke-width="3" stroke-dasharray="2.4 1.8"/>
        <circle cx="10" cy="9" r="4" fill="none" stroke="#fff" stroke-width="2.4"/>
        <circle cx="20" cy="17" r="4" fill="none" stroke="#fff" stroke-width="2.4" stroke-dasharray="2 1.5"/>
        <circle cx="20" cy="17" r="2.4" fill="none" stroke="#fff" stroke-width="1.8"/>
      </svg>
      Company Settings
    </div>
    <div class="nav-item">
      <svg viewBox="0 0 28 24"><path d="M5 21L17 9M9 3l14 16M19 3a4 4 0 1 0 4 4" fill="none" stroke="#1f2a33" stroke-width="2.4" stroke-linecap="round"/></svg>
      Configuration
    </div>
    <div class="nav-item">
      <svg viewBox="0 0 28 24"><rect x="3" y="3" width="5" height="5" fill="#1f2a33"/><rect x="10" y="3" width="15" height="5" fill="#1f2a33"/><rect x="3" y="10" width="5" height="5" fill="#1f2a33"/><rect x="10" y="10" width="15" height="5" fill="#1f2a33"/><rect x="3" y="17" width="5" height="5" fill="#1f2a33"/><rect x="10" y="17" width="15" height="5" fill="#1f2a33"/></svg>
      Services
      <svg class="chevron" viewBox="0 0 12 24"><path d="M3 7l5 5-5 5" fill="none" stroke="#1f2a33" stroke-width="2"/></svg>
    </div>
    <div class="nav-item">
      <svg viewBox="0 0 28 24"><ellipse cx="14" cy="11" rx="10" ry="7" fill="#1f2a33"/><path d="M7 16l-3 5 7-3z" fill="#1f2a33"/></svg>
      Communication
    </div>
    <div class="nav-item">
      <svg viewBox="0 0 28 24"><path d="M13 5H6v15h15v-7" fill="none" stroke="#1f2a33" stroke-width="2.4"/><path d="M12 14L22 4M16 4h6v6" fill="none" stroke="#1f2a33" stroke-width="2.4"/></svg>
      Logout
    </div>
  </nav>

  <h1 class="page-title">User Registration Form</h1>

  <main class="card">
    <p class="card-intro">Please type your account info here.</p>
    <div class="alert alert-success">Success messae</div>
    <div class="alert alert-error">Error messae</div>

    <div class="field field-username"><label>Username:</label><div class="input filled">John</div></div>
    <div class="field field-password"><label>Password:</label><div class="input password">●●●●●●●</div></div>
    <div class="field field-mail"><label>Mail:</label><div class="input">Type your mail here</div></div>
    <div class="field field-phone"><label>Phone:</label><div class="input">Type your phone here</div></div>

    <div class="check check-terms">
      <svg viewBox="0 0 22 22"><circle cx="11" cy="11" r="10" fill="#dfe3e6"/><path d="M7 11l3 3 5-5" fill="none" stroke="#4a5157" stroke-width="1.4"/></svg>
      <span>I Agree with <a href="#">Terms Of Use</a></span>
    </div>
    <div class="check check-remember">
      <svg viewBox="0 0 22 22"><circle cx="11" cy="11" r="10" fill="#dfe3e6"/><path d="M7 11l3 3 5-5" fill="none" stroke="#4a5157" stroke-width="1.4"/></svg>
      <span>Remember me</span>
    </div>

    <button class="btn-register">REGISTER</button>
  </main>

  <footer class="site-footer">
    <div class="copyright">© 2016 VORELT. All rights reserved.</div>
    <div class="footer-links">Help&nbsp; / &nbsp;Disclaimer&nbsp; / &nbsp;Contact</div>
  </footer>
</body>
</html>
```